Q-Rolls Business Card

We are a modern retail clothing store. Established in 1994. I need a presentable card that will amaze vendors when given to them.

Front: Logo in middle
Info Side:

Name: Tomas Velder
Cell: 630-812-4463
Work: 630-917-3384 EXT. 417
Email: Tomas@q-rolls-example.com
Website: www.Q-rolls-example.com

Industry/Entity Type

Business

```html
<!DOCTYPE html>
<html lang="en">
<head>
<meta charset="utf-8">
<title>Q-Rolls Business Card</title>
<link rel="stylesheet" href="https://fonts.googleapis.com/css2?family=Arimo:wght@400;700&display=swap">
<style>
  :root {
    --card-black: #030708;
    --paper-white: #ffffff;
    --ink-white: #ffffff;
  }
  html, body {
    margin: 0;
    padding: 0;
    width: 957px;
    height: 1200px;
    overflow: hidden;
    background: var(--paper-white);
    font-family: "Arimo", Arial, sans-serif;
  }
  .sheet {
    position: relative;
    width: 957px;
    height: 1200px;
  }
  .card {
    position: absolute;
    background: var(--card-black);
    color: var(--ink-white);
  }
  .card-front {
    left: 2px;
    top: 0;
    width: 955px;
    height: 552px;
  }
  .card-back {
    left: 0;
    top: 648px;
    width: 954px;
    height: 552px;
  }
  .wordmark {
    position: absolute;
    margin: 0;
    font-weight: 700;
    letter-spacing: 2px;
    line-height: 1;
    white-space: nowrap;
    color: var(--ink-white);
  }
  .front-wordmark {
    left: 0;
    right: 0;
    top: 215px;
    text-align: center;
    font-size: 118px;
  }
  .back-wordmark {
    left: 74px;
    top: 402px;
    font-size: 52px;
  }
  .holder-name {
    position: absolute;
    left: 0;
    right: 0;
    top: 215px;
    margin: 0;
    text-align: center;
    font-size: 72px;
    font-weight: 700;
    line-height: 1;
  }
  .contact-list {
    position: absolute;
    left: 521px;
    top: 372px;
    margin: 0;
    padding: 0;
    list-style: none;
    font-size: 24px;
    line-height: 32px;
    white-space: nowrap;
  }
</style>
</head>
<body>
  <main class="sheet">
    <section class="card card-front" aria-label="Card front">
      <p class="wordmark front-wordmark">Q-ROLLS</p>
    </section>

    <section class="card card-back" aria-label="Card back">
      <h1 class="holder-name">Tomas Velder</h1>
      <p class="wordmark back-wordmark">Q-ROLLS</p>
      <ul class="contact-list">
        <li>Cell: 630-812-4463</li>
        <li>Work: 630-917-3384 EXT. 417</li>
        <li>Email: Tomas@q-rolls-example.com</li>
        <li>Website: www.Q-rolls-example.com</li>
      </ul>
    </section>
  </main>
</body>
</html>
```